Scrapbooking company needs to design wordpress

We need a wordpress design. We are a workshop scrap products, we make products and courses. We would like something to convey the idea of ​​creativity, colors, paintings, clippings ...

Font styles to use
Decorative
Script

```html
<!DOCTYPE html>
<html lang="en">
<head>
<meta charset="utf-8">
<title>Bright Scraps Atelier — Blog</title>
<link href="https://fonts.googleapis.com/css2?family=Cookie&family=Dancing+Script:wght@500;700&family=Poppins:wght@300;400;500;600&display=swap" rel="stylesheet">
<style>
:root{
  --teal:#4fc6b8;
  --pink:#e4256f;
  --yellow:#f6b41a;
  --ink:#333;
  --body:#6b6b6b;
  --muted:#8a8a8a;
  --line:#dcdcdc;
  --footer:#3a3a3a;
  --white:#fff;
}
*{margin:0;padding:0;box-sizing:border-box}
html,body{width:1200px;height:4615px;overflow:hidden;background:var(--white)}
body{position:relative;font-family:'Poppins',sans-serif;color:var(--body);font-size:12.5px;line-height:22px}
.abs{position:absolute}
.hero{left:0;top:0;width:1200px;height:320px;background:linear-gradient(120deg,#5a2bb0 0%,#9b3fd6 22%,#e45fd0 40%,#6a3fe0 58%,#c54fe0 75%,#4b2aa8 100%)}
.brand{left:400px;top:170px;width:400px;text-align:center;font-family:'Poppins',sans-serif;font-weight:500;font-size:24px;letter-spacing:2px;color:var(--white);line-height:30px}
.menu{left:560px;top:298px;width:80px;text-align:center}
.menu-btn{display:block;margin:0 auto;width:34px;height:34px;border-radius:50%;background:var(--white);border:2px solid var(--teal)}
.menu-label{font-family:'Cookie',cursive;font-size:22px;color:var(--teal);line-height:22px}
.feature{left:100px;top:372px;width:720px;height:398px;border:2px solid var(--teal);display:flex}
.feature-text{width:310px;background:var(--teal);padding:60px 24px;font-family:'Dancing Script',cursive;font-weight:500;color:var(--white);font-size:33px;line-height:62px;white-space:nowrap}
.photo{background:linear-gradient(135deg,#c9a184,#8e6a52 55%,#e3d7cc)}
.post-title{font-family:'Cookie',cursive;font-weight:400;font-size:34px;color:var(--ink);border-left:4px solid var(--yellow);padding-left:22px;line-height:34px;width:720px}
.meta{font-size:11px;color:var(--muted);display:flex;gap:34px;padding-left:26px;margin-top:6px}
.meta span::before{content:"";display:inline-block;width:9px;height:9px;border:1px solid var(--muted);margin-right:8px;vertical-align:-1px}
.para{width:720px;font-size:12.5px;line-height:22px}
.para+.para{margin-top:18px}
.read{display:inline-block;background:var(--yellow);color:var(--white);font-family:'Cookie',cursive;font-size:20px;padding:2px 16px;line-height:24px}
.overlay-word{color:rgba(255,255,255,.85);font-family:'Poppins',sans-serif;font-weight:300}
.banner{left:100px;width:720px;height:278px;display:flex;align-items:center;justify-content:center;font-size:72px}
.side-text{width:322px;font-size:12.5px;line-height:24.5px;text-align:justify}
.search{left:860px;top:380px;width:238px;height:38px;border:1px solid var(--line);font-size:12px;padding:8px 14px;color:var(--muted)}
.side-head{left:860px;top:442px;font-family:'Cookie',cursive;font-weight:400;font-size:32px;color:var(--teal);white-space:nowrap}
.side-quote{left:860px;top:488px;width:238px;border-left:2px solid var(--teal);padding-left:12px;font-size:13px;line-height:24px;color:var(--body)}
.popular{left:858px;top:712px;width:242px;height:36px;border:1px solid var(--pink);font-family:'Cookie',cursive;font-weight:400;font-size:30px;color:var(--pink);padding-left:12px;line-height:36px}
.pop-img{left:858px;width:242px;height:237px;border:1px solid var(--line);display:flex;align-items:center;justify-content:center}
.date{width:78px;height:78px;border:2px solid var(--white);background:rgba(40,40,40,.55);color:var(--white);text-align:center;font-size:22px;line-height:30px;padding-top:8px}
.date small{display:block;font-size:13px;line-height:18px;border-top:1px solid var(--white);margin:4px 8px 0}
.pop-cap{left:858px;width:242px;border-left:3px solid var(--yellow);padding-left:16px}
.pop-cap h4{font-family:'Cookie',cursive;font-weight:400;font-size:24px;color:var(--ink);line-height:26px}
.pop-cap p{font-size:11.5px;line-height:18px}
.loadmore{left:100px;top:4024px;width:720px;border-bottom:1px solid var(--line);font-family:'Cookie',cursive;font-size:20px;color:var(--ink);padding-left:8px}
.comments{left:117px;top:4112px;font-family:'Cookie',cursive;font-weight:400;font-size:38px;color:var(--pink)}
.social{left:655px;top:4094px;display:flex;gap:10px}
.social i{display:block;width:36px;height:36px;border-radius:50%}
.field{left:117px;width:735px;height:37px;border:1px solid var(--line);font-size:11.5px;padding:6px 12px;color:var(--ink)}
.submit{left:117px;top:4448px;background:var(--yellow);color:var(--white);font-family:'Cookie',cursive;font-size:20px;padding:2px 22px}
.to-top{left:1025px;top:4454px;width:40px;height:40px;background:var(--yellow)}
.footer{left:0;top:4514px;width:1200px;height:101px;background:var(--footer)}
.footer-tab{left:490px;top:4478px;width:220px;height:72px;border-radius:0 0 110px 110px;background:var(--white);text-align:center;padding-top:22px;font-size:14px;font-weight:500;color:var(--pink)}
.copyright{left:0;top:4572px;width:1200px;text-align:center;color:#cfcfcf;font-size:11.5px}
</style>
</head>
<body>

<header>
  <div class="abs hero" role="img" aria-label="Purple and pink marbled paint background"></div>
  <div class="abs brand">Bright Scraps Atelier</div>
  <nav class="abs menu">
    <span class="menu-btn">
      <svg width="30" height="30" viewBox="0 0 30 30"><g stroke="#4fc6b8" stroke-width="2"><line x1="10" y1="11" x2="20" y2="11"/><line x1="10" y1="15" x2="20" y2="15"/><line x1="10" y1="19" x2="20" y2="19"/></g></svg>
    </span>
    <div class="menu-label">Menu</div>
  </nav>
</header>

<main>
  <section class="abs feature">
    <div class="feature-text">We Made<br>scrapbooking jobs<br>commissions<br>and courses</div>
    <div class="photo" style="flex:1" role="img" aria-label="Photo of a child painting a clay pot at a craft table"></div>
  </section>

  <article class="abs" style="left:100px;top:796px">
    <h2 class="post-title">Finibus Bonorum et Malorum</h2>
    <div class="meta"><span>Published on : 12 Jan 2017</span><span>Ada Marsh</span><span>Inspiration</span></div>
    <p class="para" style="margin-top:16px">Sed ut perspiciatis unde omnis iste natus error sit voluptatem accusantium doloremque laudantium, totam rem aperiam, eaque ipsa quae ab illo inventore veritatis et quasi architecto beatae vitae dicta sunt explicabo. Nemo enim ipsam voluptatem quia voluptas sit aspernatur aut odit aut fugit, sed quia consequuntur magni dolores eos qui ratione voluptatem sequi nesciunt. Neque porro quisquam est, qui dolorem ipsum quia dolor sit amet, consectetur, adipisci velit, sed quia non numquam eius modi tempora incidunt.</p>
    <p class="para">Ut labore et dolore magnam aliquam quaerat voluptatem. Ut enim ad minima veniam, quis nostrum exercitationem ullam corporis suscipit laboriosam, nisi ut aliquid ex ea commodi consequatur? Quis autem vel eum iure reprehenderit qui in ea voluptate velit esse quam nihil molestiae consequatur, vel illum qui dolorem eum fugiat quo voluptas nulla pariatur.</p>
  </article>
  <div class="abs photo" style="left:130px;top:1155px;width:330px;height:323px;background:radial-gradient(circle,#f2c66a,#d9883a 45%,#b44d3a 70%,#f3efe6 72%);display:flex;align-items:center;justify-content:center;font-size:48px" role="img" aria-label="Colored pencils arranged in a circle"><span class="overlay-word">Colors</span></div>
  <div class="abs side-text" style="left:483px;top:1150px">Sed ut perspiciatis unde omnis iste natus error sit voluptatem accusantium doloremque laudantium, totam rem aperiam, eaque ipsa quae ab illo inventore veritatis et quasi architecto beatae vitae dicta sunt explicabo. Nemo enim ipsam voluptatem quia voluptas sit aspernatur aut odit aut fugit, sed quia consequuntur magni dolores eos qui ratione voluptatem sequi nesciunt. Neque porro quisquam est, qui dolorem ipsum quia dolor sit amet, consectetur, adipisci velit, sed quia non numquam eius modi tempora incidunt<br><br>Ut labore et dolore magnam aliquam quaerat voluptatem. Ut enim ad minima veniam,</div>
  <a class="abs read" style="left:483px;top:1500px">Read more</a>

  <div class="abs banner" style="top:1560px;background:linear-gradient(90deg,#6b3a1e,#8a5430 45%,#5a7a2a 75%,#3e5e22)" role="img" aria-label="Holiday newspaper clippings on a wooden board"><span class="overlay-word">Clippings</span></div>

  <article class="abs" style="left:100px;top:1873px">
    <h2 class="post-title">Finibus Bonorum et Malorum</h2>
    <div class="meta"><span>Published on : 12 Jan 2017</span><span>Ada Marsh</span><span>Inspiration</span></div>
    <p class="para" style="margin-top:16px">Sed ut perspiciatis unde omnis iste natus error sit voluptatem accusantium doloremque laudantium, totam rem aperiam, eaque ipsa quae ab illo inventore veritatis et quasi architecto beatae vitae dicta sunt explicabo. Nemo enim ipsam voluptatem quia voluptas sit aspernatur aut odit aut fugit, sed quia consequuntur magni dolores eos qui ratione voluptatem sequi nesciunt. Neque porro quisquam est, qui dolorem ipsum quia dolor sit amet, consectetur, adipisci velit, sed quia non numquam eius modi tempora incidunt.</p>
    <p class="para">Ut labore et dolore magnam aliquam quaerat voluptatem. Ut enim ad minima veniam, quis nostrum exercitationem ullam corporis suscipit laboriosam, nisi ut aliquid ex ea commodi consequatur? Quis autem vel eum iure reprehenderit qui in ea voluptate velit esse quam nihil molestiae consequatur, vel illum qui dolorem eum fugiat quo voluptas nulla pariatur.</p>
  </article>
  <a class="abs read" style="left:126px;top:2212px">Read more</a>

  <article class="abs" style="left:100px;top:2295px">
    <h2 class="post-title">Finibus Bonorum et Malorum</h2>
    <div class="meta"><span>Published on : 12 Jan 2017</span><span>Ada Marsh</span><span>Inspiration</span></div>
  </article>
  <div class="abs photo" style="left:130px;top:2385px;width:325px;height:323px;background:linear-gradient(135deg,#e94f3a,#f2b33a 35%,#3a9bd6 65%,#8a3ab0);display:flex;align-items:center;justify-content:flex-end;font-size:44px" role="img" aria-label="Colorful abstract watercolor portrait painting"><span class="overlay-word" style="writing-mode:vertical-rl">Paintings</span></div>
  <div class="abs side-text" style="left:488px;top:2385px">Sed ut perspiciatis unde omnis iste natus error sit voluptatem accusantium doloremque laudantium, totam rem aperiam, eaque ipsa quae ab illo inventore veritatis et quasi architecto beatae vitae dicta sunt explicabo. Nemo enim ipsam voluptatem quia voluptas sit aspernatur aut odit aut fugit, sed quia consequuntur magni dolores eos qui ratione voluptatem sequi nesciunt. Neque porro quisquam est, qui dolorem ipsum quia dolor sit amet, consectetur, adipisci velit, sed quia non numquam eius modi tempora incidunt<br><br>Ut labore et dolore magnam aliquam quaerat voluptatem. Ut enim ad minima veniam,</div>
  <a class="abs read" style="left:488px;top:2735px">Read more</a>

  <div class="abs banner" style="top:2788px;background:linear-gradient(135deg,#d8dde2,#aeb6bd 50%,#e6e9ec)" role="img" aria-label="Layered paper cut-out clipping shapes"><span class="overlay-word">Clippings</span></div>

  <article class="abs" style="left:100px;top:3101px">
    <h2 class="post-title">Finibus Bonorum et Malorum</h2>
    <div class="meta"><span>Published on : 12 Jan 2017</span><span>Ada Marsh</span><span>Inspiration</span></div>
    <p class="para" style="margin-top:16px">Sed ut perspiciatis unde omnis iste natus error sit voluptatem accusantium doloremque laudantium, totam rem aperiam, eaque ipsa quae ab illo inventore veritatis et quasi architecto beatae vitae dicta sunt explicabo. Nemo enim ipsam voluptatem quia voluptas sit aspernatur aut odit aut fugit, sed quia consequuntur magni dolores eos qui ratione voluptatem sequi nesciunt. Neque porro quisquam est, qui dolorem ipsum quia dolor sit amet, consectetur, adipisci velit, sed quia non numquam eius modi tempora incidunt.</p>
    <p class="para">Ut labore et dolore magnam aliquam quaerat voluptatem. Ut enim ad minima veniam, quis nostrum exercitationem ullam corporis suscipit laboriosam, nisi ut aliquid ex ea commodi consequatur? Quis autem vel eum iure reprehenderit qui in ea voluptate velit esse quam nihil molestiae consequatur, vel illum qui dolorem eum fugiat quo voluptas nulla pariatur.</p>
  </article>
  <a class="abs read" style="left:126px;top:3442px">Read more</a>

  <article class="abs" style="left:100px;top:3522px">
    <h2 class="post-title">Finibus Bonorum et Malorum</h2>
    <div class="meta"><span>Published on : 12 Jan 2017</span><span>Ada Marsh</span><span>Inspiration</span></div>
  </article>
  <div class="abs photo" style="left:130px;top:3606px;width:325px;height:332px;background:linear-gradient(160deg,#f6eee9,#e3584a 40%,#f0d6cf 75%,#fff);display:flex;align-items:center;justify-content:flex-end;font-size:44px" role="img" aria-label="Red watercolor flower painting"><span class="overlay-word" style="writing-mode:vertical-rl;color:rgba(60,60,60,.8)">Paintings</span></div>
  <div class="abs side-text" style="left:488px;top:3600px">Sed ut perspiciatis unde omnis iste natus error sit voluptatem accusantium doloremque laudantium, totam rem aperiam, eaque ipsa quae ab illo inventore veritatis et quasi architecto beatae vitae dicta sunt explicabo. Nemo enim ipsam voluptatem quia voluptas sit aspernatur aut odit aut fugit, sed quia consequuntur magni dolores eos qui ratione voluptatem sequi nesciunt. Neque porro quisquam est, qui dolorem ipsum quia dolor sit amet, consectetur, adipisci velit, sed quia non numquam eius modi tempora incidunt<br><br>Ut labore et dolore magnam aliquam quaerat voluptatem. Ut enim ad minima veniam,</div>
  <a class="abs read" style="left:488px;top:3962px">Read more</a>

  <div class="abs loadmore">Load more...</div>

  <section>
    <h3 class="abs comments">Comments</h3>
    <div class="abs social">
      <i style="background:#2b5aa8"></i><i style="background:#2aa3e0"></i><i style="background:#d62a2a"></i><i style="background:#a5773f"></i>
    </div>
    <div class="abs field" style="top:4188px">Name</div>
    <div class="abs field" style="top:4250px">Email</div>
    <div class="abs field" style="top:4311px">Phone</div>
    <div class="abs field" style="top:4360px;height:76px">Message</div>
    <a class="abs submit">Submit</a>
  </section>
</main>

<aside>
  <div class="abs search">Search here
    <svg class="abs" style="right:12px;top:12px" width="12" height="12" viewBox="0 0 12 12"><circle cx="5" cy="5" r="3.8" fill="none" stroke="#555" stroke-width="1.5"/><line x1="8" y1="8" x2="11" y2="11" stroke="#555" stroke-width="1.5"/></svg>
  </div>
  <h3 class="abs side-head">Bright Scraps Atelier</h3>
  <p class="abs side-quote">" Lorem ipsum dolor sit amet, consectetur adipisicing elit, sed do eiusmod tempor incididunt ut labore et dolore magna aliqua. Ut enim ad minim veniam, quis nostrud."</p>
  <h3 class="abs popular">Popular Post</h3>

  <div class="abs pop-img" style="top:758px;height:300px;background:linear-gradient(135deg,#f25a3a,#f6c23a 40%,#3ab0d6 75%,#9a3ad6)" role="img" aria-label="Colorful painted flower"><div class="date">01<small>JAN</small></div></div>
  <div class="abs pop-cap" style="top:1075px"><h4>Finibus Bonorum et Malorum</h4><p>Sed ut perspiciatis unde omnis iste natus error sit voluptatem accusantium doloremque laudantium,</p></div>

  <div class="abs pop-img" style="top:1228px;background:linear-gradient(135deg,#f4eef2,#d7a6c9 45%,#c6d3ea)" role="img" aria-label="Pale watercolor flower"><div class="date">01<small>JAN</small></div></div>
  <div class="abs pop-cap" style="top:1480px"><h4>Finibus Bonorum et Malorum</h4><p>Sed ut perspiciatis unde omnis iste natus error sit voluptatem accusantium doloremque laudantium,</p></div>

  <div class="abs pop-img" style="top:1608px;background:linear-gradient(135deg,#2b2b2b,#5a6a70 50%,#d04a3a)" role="img" aria-label="Painted butterfly wing"><div class="date">01<small>JAN</small></div></div>
  <div class="abs pop-cap" style="top:1860px"><h4>Finibus Bonorum et Malorum</h4><p>Sed ut perspiciatis unde omnis iste natus error sit voluptatem accusantium doloremque laudantium,</p></div>

  <div class="abs pop-img" style="top:1988px;background:linear-gradient(135deg,#fff,#e8235f 35%,#c8104a 65%,#fff)" role="img" aria-label="Pink paint brush stroke"><div class="date">01<small>JAN</small></div></div>
  <div class="abs pop-cap" style="top:2240px"><h4>Finibus Bonorum et Malorum</h4><p>Sed ut perspiciatis unde omnis iste natus error sit voluptatem accusantium doloremque laudantium,</p></div>

  <div class="abs pop-img" style="top:2368px;background:linear-gradient(135deg,#dbe9ee,#7fb4c6 50%,#3d6c7e)" role="img" aria-label="Blue paint tube sketch"><div class="date">01<small>JAN</small></div></div>
  <div class="abs pop-cap" style="top:2620px"><h4>Finibus Bonorum et Malorum</h4><p>Sed ut perspiciatis unde omnis iste natus error sit voluptatem accusantium doloremque laudantium,</p></div>
</aside>

<a class="abs to-top">
  <svg width="40" height="40" viewBox="0 0 40 40"><polyline points="14,23 20,17 26,23" fill="none" stroke="#333" stroke-width="2"/></svg>
</a>

<footer>
  <div class="abs footer"></div>
  <div class="abs footer-tab">Bright Scraps Atelier</div>
  <p class="abs copyright">Copyrights © 2017 - All Rights Reserved</p>
</footer>

</body>
</html>
```